Tri-fold Brochure Design for Banking Business

The brochure we have needs to be improved - more business like and more attractive. Logo file and brochure is attached. I would like to be able to edit the text after you get done. Your ideas and changes to text are welcome. See our website www.korvanbridgegrp.com for our theme. We can use indesign to edit the text after you complete. However, please make changes to the text we have in the design that it uploaded. Your comments and changes are welcome.

Target Market(s)

Human Resources and learning & development staff at the global investment banks - Pellham Trask, QWNR, etc.

Industry/Entity Type

Investment Banking

Logo Text

Korvan Bridge Group

Font styles to use
Serif
Sans Serif

Colors
33a6d7
0493ce
3277b5
fbf289
fdf9cf
fbee3e
0555a3
85acd3

Requirements
Must have
• Must be similar to our website www.korvanbridgegrp.com. Needs to be business-like, clean fonts, sharp design. Our logo - of course.
Nice to have
• City images - seems to be our theme.

```html
<!DOCTYPE html>
<html lang="en">
<head>
<meta charset="utf-8">
<title>Korvan Bridge Group – Tri-fold Brochure</title>
<link href="https://fonts.googleapis.com/css2?family=Oswald:wght@300;400;600&family=Montserrat:wght@400;600;700;800&display=swap" rel="stylesheet">
<style>
  :root{
    --blue:#0b4c9e;
    --blue-deep:#083a80;
    --blue-soft:#85acd3;
    --sky:#cfe3f4;
    --yellow:#f5d21b;
    --paper:#ffffff;
    --grey:#eceef1;
    --ink:#1e2a3a;
    --stage:#d9dadc;
  }
  *{box-sizing:border-box;margin:0;padding:0}
  html,body{width:855px;height:1200px;overflow:hidden;background:var(--stage)}
  body{position:relative;font-family:"Montserrat",sans-serif;color:var(--ink)}
  .spread{position:absolute;left:30px;width:795px;height:520px;display:flex;box-shadow:0 6px 18px rgba(0,0,0,.18)}
  .spread--outside{top:36px}
  .spread--inside{top:628px}
  .side-label{position:absolute;font-family:"Montserrat",sans-serif;font-size:17px;letter-spacing:1px;color:#222}
  .side-label--outside{top:566px;right:32px}
  .side-label--inside{top:1160px;left:32px}
  .panel{position:relative;width:265px;height:520px;overflow:hidden}
  .panel svg.bg{position:absolute;inset:0}
  .abs{position:absolute}
  .heading{font-family:"Oswald",sans-serif;text-transform:uppercase;line-height:1}
  .heading .light{font-weight:300}
  .heading .bold{font-weight:600}
  .body-copy{font-size:8px;line-height:1.55}
  .url-tag{position:absolute;background:var(--yellow);color:var(--blue-deep);font-family:"Oswald",sans-serif;font-weight:600;font-size:10px;letter-spacing:.4px;padding:3px 9px;text-transform:uppercase}
  .url-plain{font-family:"Oswald",sans-serif;font-weight:400;font-size:13px;color:var(--blue);text-transform:uppercase;text-align:center}
  .logo{font-family:"Oswald",sans-serif;font-weight:600;color:var(--blue-deep);text-transform:uppercase;display:flex;align-items:center;gap:8px;letter-spacing:1px}
  .logo .mark{flex:0 0 14px;width:14px;height:14px;background:var(--yellow)}
  .icon-ring{position:absolute;width:34px;height:34px;border-radius:50%;border:2px solid var(--blue-soft);display:flex;align-items:center;justify-content:center;background:#fff}

  /* outside: about */
  .about-title{left:24px;top:286px;font-size:26px;color:var(--yellow)}
  .about-copy{left:24px;top:322px;width:222px;color:#fff}
  .about-copy p{margin-bottom:9px}

  /* outside: contact */
  .panel--contact{background:var(--grey)}
  .contact-title{top:22px;width:100%;text-align:center;font-size:22px;color:var(--blue)}
  .contact-list{top:110px;width:100%;text-align:center}
  .contact-list dt{font-size:8px;font-weight:700;color:var(--blue);text-transform:uppercase;margin-top:7px}
  .contact-list dd{font-size:8px;color:#333}
  .worldwide{top:360px;width:100%;text-align:center}
  .worldwide .big{font-family:"Montserrat",sans-serif;font-weight:800;font-size:22px;color:var(--blue);letter-spacing:.5px}
  .worldwide .small{font-family:"Montserrat",sans-serif;font-weight:700;font-size:12px;color:#4a4f57;letter-spacing:1px}

  /* outside: cover */
  .panel--cover{background:var(--sky)}
  .cover-headline{left:22px;top:390px;width:225px;color:#fff}
  .cover-headline .line1{font-size:15px;font-weight:300}
  .cover-headline .line2{font-size:24px;font-weight:600;color:var(--yellow)}

  /* inside: why */
  .panel--why{background:var(--paper)}
  .why-title{left:24px;top:196px;font-size:22px;color:var(--blue)}
  .why-copy{left:24px;top:232px;width:220px}
  .why-copy p{margin-bottom:7px}
  .why-list{list-style:none;left:24px;top:300px;width:222px}
  .why-list li{display:flex;gap:8px;font-size:9px;font-weight:700;line-height:1.35;margin-bottom:9px}
  .tick{flex:0 0 13px;height:13px;border-radius:50%;background:var(--yellow);display:flex;align-items:center;justify-content:center}

  /* inside: services */
  .panel--services{background:var(--blue)}
  .services-title{top:228px;width:100%;text-align:center;font-size:24px;color:#fff}
  .services-title .bold{color:var(--yellow)}
  .services-copy{left:26px;top:266px;width:214px;color:#fff;text-align:center}
  .services-copy p{margin-bottom:8px}

  /* inside: team */
  .panel--team{background:var(--paper)}
  .team-title{top:30px;width:100%;text-align:center;font-size:22px;color:var(--blue)}
  .team-copy{left:26px;top:68px;width:214px;text-align:center;font-size:7.5px}
  .team-copy p{margin-bottom:8px}
  .contact-box{left:36px;top:160px;width:194px;border-top:1px dashed var(--blue-soft);border-bottom:1px dashed var(--blue-soft);padding:6px 0;text-align:center}
  .contact-box .ask{font-size:8px;font-weight:700;letter-spacing:.5px}
  .contact-box .cta{font-size:19px;font-weight:800;color:var(--blue);text-transform:uppercase}
</style>
</head>
<body>

<!-- OUTSIDE SPREAD -->
<section class="spread spread--outside" aria-label="Brochure outside">

  <article class="panel panel--about">
    <svg class="bg" width="265" height="520" viewBox="0 0 265 520">
      <defs>
        <linearGradient id="skyline1" x1="0" y1="0" x2="0" y2="1">
          <stop offset="0" stop-color="#7fb2e0"/><stop offset=".55" stop-color="#9aa3ac"/><stop offset="1" stop-color="#4d6a86"/>
        </linearGradient>
        <linearGradient id="circleShot" x1="0" y1="0" x2="0" y2="1">
          <stop offset="0" stop-color="#d7c7ae"/><stop offset="1" stop-color="#56708a"/>
        </linearGradient>
      </defs>
      <rect x="0" y="0" width="265" height="275" fill="url(#skyline1)" role="img" aria-label="Photo of a city skyline across the water"/>
      <polygon points="0,12 265,0 265,6 0,18" fill="var(--blue)"/>
      <rect x="20" y="14" width="22" height="5" fill="var(--yellow)"/>
      <polygon points="150,254 265,214 265,282" fill="#c7d8ea"/>
      <polygon points="0,272 265,242 265,520 0,520" fill="var(--blue)"/>
      <polygon points="230,226 250,244 222,244" fill="var(--yellow)"/>
      <circle cx="72" cy="230" r="44" fill="url(#circleShot)" stroke="#fff" stroke-width="4" role="img" aria-label="Photo of a riverside city tower"/>
      <line x1="0" y1="508" x2="265" y2="508" stroke="#fff" stroke-width="1" stroke-dasharray="3 2"/>
    </svg>
    <h2 class="abs heading about-title"><span class="bold">About Us</span></h2>
    <div class="abs body-copy about-copy">
      <p><strong>Korvan Bridge Group</strong> efficiently provides complete sales, marketing and logistical support for all our programs, no matter the location.</p>
      <p>Our globally located trainers have extensive experience, both as industry professionals and as trainers.</p>
      <p>Our highly qualified logistical team complement the training services, providing reliable and efficient support.</p>
    </div>
    <span class="url-tag" style="left:40px;top:480px">www.korvanbridgegrp.com</span>
  </article>

  <article class="panel panel--contact">
    <h2 class="abs heading contact-title"><span class="light">Get in </span><span class="bold">Touch</span></h2>
    <div class="icon-ring" style="left:115px;top:58px">
      <svg width="18" height="14" viewBox="0 0 18 14"><rect x="1" y="1" width="16" height="12" fill="none" stroke="var(--blue)" stroke-width="1.5"/><polyline points="1,1 9,8 17,1" fill="none" stroke="var(--blue)" stroke-width="1.5"/></svg>
    </div>
    <dl class="abs contact-list">
      <dt>Global</dt><dd>elena.marsh@korvanbridgegrp.com</dd>
      <dt>Asia</dt><dd>paul.kessler@korvanbridgegrp.com</dd>
      <dt>United States</dt><dd>rick.amato@korvanbridgegrp.com</dd>
      <dt>Europe</dt><dd>sean.dorley@korvanbridgegrp.com</dd>
    </dl>
    <div class="abs" style="left:40px;top:256px;width:185px;height:90px;background:linear-gradient(180deg,#b9bcc0,#9a9ea3);border-radius:40px/30px" role="img" aria-label="Grey world map"></div>
    <div class="abs worldwide">
      <div class="big">WORLDWIDE</div>
      <div class="small">TRAINING SERVICE</div>
    </div>
    <div class="icon-ring" style="left:115px;top:420px">
      <svg width="18" height="18" viewBox="0 0 18 18" fill="none" stroke="var(--blue)" stroke-width="1.3"><circle cx="9" cy="9" r="7.5"/><ellipse cx="9" cy="9" rx="3.5" ry="7.5"/><line x1="1.5" y1="9" x2="16.5" y2="9"/><line x1="3" y1="5" x2="15" y2="5"/><line x1="3" y1="13" x2="15" y2="13"/></svg>
    </div>
    <div class="abs url-plain" style="top:470px;width:100%">www.korvanbridgegrp.com</div>
  </article>

  <article class="panel panel--cover">
    <svg class="bg" width="265" height="520" viewBox="0 0 265 520">
      <defs>
        <linearGradient id="skyline2" x1="0" y1="0" x2="0" y2="1">
          <stop offset="0" stop-color="#d5e6f3"/><stop offset=".5" stop-color="#7f98ae"/><stop offset="1" stop-color="#3d5670"/>
        </linearGradient>
      </defs>
      <rect x="0" y="0" width="265" height="8" fill="var(--blue)"/>
      <rect x="210" y="0" width="24" height="8" fill="var(--yellow)"/>
      <polygon points="20,80 265,80 265,340 200,320 20,300" fill="url(#skyline2)" role="img" aria-label="Photo of a harbour city with glass towers"/>
      <polygon points="0,320 150,330 230,270 265,250 265,520 0,520" fill="var(--blue)"/>
      <polygon points="240,248 265,236 265,262" fill="var(--yellow)"/>
      <polygon points="150,330 230,270 238,278 160,338" fill="#c7d8ea"/>
    </svg>
    <div class="abs logo" style="left:38px;top:30px;width:200px;font-size:20px"><span class="mark"></span>Korvan Bridge Group</div>
    <h1 class="abs heading cover-headline"><span class="line1">Your expert training and</span><br><span class="line2">Consulting Partner</span></h1>
    <span class="url-tag" style="left:80px;top:456px">www.korvanbridgegrp.com</span>
  </article>
</section>
<div class="side-label side-label--outside">OUTSIDE</div>

<!-- INSIDE SPREAD -->
<section class="spread spread--inside" aria-label="Brochure inside">

  <article class="panel panel--why">
    <svg class="bg" width="265" height="520" viewBox="0 0 265 520">
      <defs>
        <linearGradient id="signShot" x1="0" y1="0" x2="1" y2="1">
          <stop offset="0" stop-color="#c9cbce"/><stop offset=".5" stop-color="#3b3d42"/><stop offset="1" stop-color="#16171a"/>
        </linearGradient>
      </defs>
      <rect x="0" y="0" width="265" height="8" fill="var(--blue)"/>
      <rect x="30" y="0" width="22" height="8" fill="var(--yellow)"/>
      <polygon points="0,8 265,8 265,190 0,150" fill="url(#signShot)" role="img" aria-label="Photo of an illuminated company sign on a dark wall"/>
      <polygon points="0,150 265,190 265,205 0,165" fill="var(--blue)"/>
      <line x1="0" y1="508" x2="265" y2="508" stroke="var(--blue-soft)" stroke-width="1" stroke-dasharray="3 2"/>
    </svg>
    <div class="abs logo" style="left:110px;top:62px;width:140px;font-size:14px;color:#fff">Korvan Bridge Group</div>
    <h2 class="abs heading why-title"><span class="light">Why </span><span class="bold">Choose Us?</span></h2>
    <div class="abs body-copy why-copy" style="font-size:7.5px">
      <p>Korvan Bridge Group is dedicated to providing you and your firm with the highest level of service.</p>
      <p>We provide dedicated sales and logistics support for each program to insure consistent, reliable results.</p>
    </div>
    <ul class="abs why-list">
      <li><span class="tick"><svg width="8" height="7" viewBox="0 0 8 7"><polyline points="1,3.5 3,5.5 7,1" fill="none" stroke="#fff" stroke-width="1.5"/></svg></span>Highly qualified, international pool of trainers.</li>
      <li><span class="tick"><svg width="8" height="7" viewBox="0 0 8 7"><polyline points="1,3.5 3,5.5 7,1" fill="none" stroke="#fff" stroke-width="1.5"/></svg></span>Strong client relationship management and support</li>
      <li><span class="tick"><svg width="8" height="7" viewBox="0 0 8 7"><polyline points="1,3.5 3,5.5 7,1" fill="none" stroke="#fff" stroke-width="1.5"/></svg></span>Competitive pricing and flexibility.</li>
      <li><span class="tick"><svg width="8" height="7" viewBox="0 0 8 7"><polyline points="1,3.5 3,5.5 7,1" fill="none" stroke="#fff" stroke-width="1.5"/></svg></span>Outcome driven approach directly matches your company's needs.</li>
    </ul>
    <span class="url-tag" style="left:24px;top:472px">www.korvanbridgegrp.com</span>
  </article>

  <article class="panel panel--services">
    <svg class="bg" width="265" height="520" viewBox="0 0 265 520">
      <defs>
        <linearGradient id="trainShot" x1="0" y1="0" x2="1" y2="1">
          <stop offset="0" stop-color="#bfe0f5"/><stop offset="1" stop-color="#2f78b8"/>
        </linearGradient>
        <linearGradient id="handShot" x1="0" y1="0" x2="1" y2="1">
          <stop offset="0" stop-color="#5c5f66"/><stop offset="1" stop-color="#1a1b1e"/>
        </linearGradient>
      </defs>
      <rect x="0" y="0" width="265" height="6" fill="var(--yellow)"/>
      <circle cx="120" cy="96" r="60" fill="url(#trainShot)" stroke="#fff" stroke-width="4" role="img" aria-label="Photo of a hand touching a training concept screen"/>
      <circle cx="190" cy="156" r="30" fill="url(#handShot)" stroke="#fff" stroke-width="3" role="img" aria-label="Photo of a business handshake"/>
    </svg>
    <h2 class="abs heading services-title"><span class="light">Our </span><span class="bold">Services</span></h2>
    <div class="abs body-copy services-copy" style="font-size:7.5px">
      <p>Korvan Bridge Group provides best in class services for all our clients. We provide highly customized programs tailored to your specific requirements.</p>
      <p>Direct interaction between our clients, consulting trainers and client servicestaff ensures measurable outcomes for program participants.</p>
      <p>We facilitate learning outcomes using a blended methodology combining interactive analysis, hands-on experiential models, market simulations and a state-of-the-art learning management system.</p>
      <p>Our material databanks are continuously updated to insure accuracy and effectiveness of our services.</p>
    </div>
    <div class="icon-ring" style="left:115px;top:446px;background:transparent;border-color:#fff">
      <svg width="18" height="18" viewBox="0 0 18 18" fill="none" stroke="#fff" stroke-width="1.3"><circle cx="9" cy="9" r="7.5"/><ellipse cx="9" cy="9" rx="3.5" ry="7.5"/><line x1="1.5" y1="9" x2="16.5" y2="9"/><line x1="3" y1="5" x2="15" y2="5"/><line x1="3" y1="13" x2="15" y2="13"/></svg>
    </div>
    <div class="abs url-plain" style="top:488px;width:100%;color:#fff">www.korvanbridgegrp.com</div>
  </article>

  <article class="panel panel--team">
    <svg class="bg" width="265" height="520" viewBox="0 0 265 520">
      <defs>
        <linearGradient id="teamShot" x1="0" y1="0" x2="0" y2="1">
          <stop offset="0" stop-color="#d9e6f2"/><stop offset=".6" stop-color="#6f8aa6"/><stop offset="1" stop-color="#2d4a6b"/>
        </linearGradient>
      </defs>
      <rect x="0" y="0" width="265" height="8" fill="var(--blue)"/>
      <rect x="225" y="0" width="24" height="8" fill="var(--yellow)"/>
      <polygon points="0,300 265,330 265,520 0,520" fill="url(#teamShot)" role="img" aria-label="Photo of a business team standing on a globe"/>
      <polygon points="0,286 265,316 265,332 0,302" fill="var(--blue)"/>
    </svg>
    <h2 class="abs heading team-title"><span class="light">Our </span><span class="bold">Team</span></h2>
    <div class="abs body-copy team-copy">
      <p>Our Consulting Trainers are located globally and recognized by the industry as highly effective trainers and program facilitators.</p>
      <p><strong>Korvan</strong> provides global expertise for our programs with local talent for program facilitation.</p>
    </div>
    <div class="abs contact-box">
      <div class="ask">NEED MORE INFORMATION?</div>
      <div class="cta">Contact Us!</div>
    </div>
    <div class="abs logo" style="left:40px;top:236px;font-size:17px"><span class="mark"></span>Korvan Bridge Group</div>
    <span class="url-tag" style="left:60px;top:482px">www.korvanbridgegrp.com</span>
  </article>
</section>
<div class="side-label side-label--inside">INSIDE</div>

</body>
</html>
```